依頼詳細
ホームページの開設に合わせて、「A5サイズの簡易版のチラシ」と、「A4サイズのチラシ」の2つの作成をお願いします。
ホームページは公開されていないので、ランディングページのPDFデータを添付します。
イラストやロゴなど、PDFデータから必要な部分をコピーして作成していただければ結構です。

PDF以外のイラストや写真なども使用していただけますが、雰囲気や色味は変えないようにしてください。

ご質問などございましたらお気軽にご連絡ください。
記載項目
屋号・電話番号・QRコード・ロゴ・遺品整理・生前整理・お買取り・見積り無料など。
必ず記載していただきたい内容は、添付ファイルに記載しておりますのでご覧ください。
サイズ
A4
ページ数
片面
希望イメージ
シンプル 複雑
単色 カラフル
暗い 明るい
日常 高級
遊び心 厳粛
未来的 伝統的
女性的 男性的
希望する色
黄・オレンジ系
納品ファイル
• イラストレーター形式 (.ai)
補足説明
納品はCS6以下、アウトライン前後のデータで納品してください。
ランディングページのPDFデータは添付できなかったので、下記アドレスからダウンロードしてください。
https://48.hakobunet.jp/3030-e7d19a04c6b2f85d3e10ab97c4d2e6f81
この度はたくさんのご提案を頂きまして、ありがとうございます。
社内で検討・選定いたしますので、しばらくお待ちくださいませ。
宜しくお願い致します。
■ 選んだ理由

この度は、弊社の遺品整理チラシにご提案いただきありがとうございました。
選定はとても迷ったのですが、mofu-83様のご提案は、オレンジに白文字で遺品整理と大きく書かれてとても印象的でしたし、全体的にメリハリが効いていたことが選定の決め手になりました。

■ 提案者全員のお礼・コメント

この度は、たくさんのコンペの中から遺品整理チラシにご提案いただきましてありがとうございました。同じ依頼でもこんなにも多様なご提案を頂け、コトノバー様のスキルに驚かされました。
今後も不定期ではございますが、コトノバを利用させていただきますので、ぜひご提案いただけましたら幸いです。
この度は本当にありがとうございました。

```html
<!DOCTYPE html>
<html lang="ja">
<head>
<meta charset="utf-8">
<title>遺品整理・生前整理 チラシ</title>
<link href="https://fonts.googleapis.com/css2?family=M+PLUS+Rounded+1c:wght@400;700;800&family=Noto+Sans+JP:wght@400;500;700&display=swap" rel="stylesheet">
<style>
:root{
  --orange:#f08c2c;
  --orange-deep:#e4761a;
  --peach:#fbe4cf;
  --peach-soft:#fdf1e6;
  --ink:#4a3a2e;
  --grey:#6b6b6b;
  --white:#ffffff;
  --illust-a:#f6c48f;
  --illust-b:#fbe0c4;
}
*{margin:0;padding:0;box-sizing:border-box}
html,body{width:847px;height:1200px;overflow:hidden;background:var(--white)}
body{font-family:"Noto Sans JP",sans-serif;color:var(--ink);position:relative}
.flyer{position:relative;width:847px;height:1200px;background:var(--white)}
.hero-illust{position:absolute;left:40px;top:20px;width:767px;height:420px;border-radius:20px;
  background:radial-gradient(ellipse at center,var(--peach-soft) 0%,var(--white) 75%)}
.headline{position:absolute;left:0;right:0;top:120px;text-align:center;
  font-family:"M PLUS Rounded 1c",sans-serif;font-weight:800;color:var(--orange);letter-spacing:.06em}
.headline .l1{font-size:36px;line-height:1.4}
.headline .l2{font-size:36px;line-height:1.4}
.headline .l2 em{font-style:normal;color:var(--orange-deep)}
.hero-scene{position:absolute;left:210px;top:290px;width:427px;height:130px;border-radius:12px;
  background:linear-gradient(90deg,var(--illust-b),var(--illust-a),var(--illust-b))}
.lower{position:absolute;left:0;top:440px;width:847px;height:555px;background:var(--peach)}
.services{position:absolute;left:52px;top:470px;width:743px;display:flex;gap:22px}
.card{flex:1;background:var(--white);border-radius:6px;padding:14px 14px 16px;height:270px}
.card .pic{height:96px;border-radius:6px;background:linear-gradient(180deg,var(--illust-b),var(--illust-a))}
.card .label{margin:10px 0 8px;background:var(--orange);color:var(--white);
  font-family:"M PLUS Rounded 1c",sans-serif;font-weight:800;font-size:19px;text-align:center;
  padding:5px 0;border-radius:3px;letter-spacing:.08em}
.card p{font-size:10.5px;line-height:1.75;color:var(--grey)}
.recommend{position:absolute;left:52px;top:770px;width:743px;height:160px;
  border:2px solid var(--orange);border-radius:8px;background:var(--white)}
.recommend h2{position:absolute;left:-2px;top:-22px;background:var(--orange);color:var(--white);
  font-family:"M PLUS Rounded 1c",sans-serif;font-size:16px;font-weight:800;padding:4px 18px;border-radius:6px 6px 0 0}
.bubble{position:absolute;top:14px;background:var(--peach-soft);border:1.5px solid var(--orange);
  border-radius:50%;width:120px;height:70px;display:flex;align-items:center;justify-content:center;
  text-align:center;font-size:10.5px;line-height:1.4;font-weight:500}
.person{position:absolute;bottom:10px;width:70px;height:58px;border-radius:35px 35px 8px 8px;background:var(--illust-a)}
.free{position:absolute;right:20px;top:28px;width:104px;height:104px;border-radius:50%;background:var(--orange);
  color:var(--white);font-family:"M PLUS Rounded 1c",sans-serif;font-weight:800;font-size:22px;
  display:flex;align-items:center;justify-content:center;text-align:center;line-height:1.25}
.footnote{position:absolute;left:0;top:948px;width:847px;height:34px;background:var(--orange);color:var(--white);
  font-size:13.5px;font-weight:500;display:flex;align-items:center;justify-content:center;letter-spacing:.03em}
.bottom{position:absolute;left:52px;right:52px;top:1020px;height:150px;display:flex;justify-content:space-between;align-items:center}
.brand{display:flex;align-items:center;gap:14px}
.badge{width:44px;height:44px;background:var(--orange)}
.brand-name{font-family:"M PLUS Rounded 1c",sans-serif;font-weight:800;color:var(--orange-deep);font-size:28px;letter-spacing:.06em;line-height:1.15}
.brand-name span{display:block;font-size:17px}
.contact{text-align:left}
.tel{display:flex;align-items:center;gap:10px;font-family:"M PLUS Rounded 1c",sans-serif;font-weight:800;font-size:38px;color:var(--orange-deep)}
.tel svg{width:36px;height:36px}
.info{font-size:13px;color:var(--ink);margin-top:4px;display:flex;gap:22px}
.info b{background:var(--ink);color:var(--white);font-weight:500;padding:1px 6px;margin-right:4px}
</style>
</head>
<body>
<div class="flyer">
  <div class="hero-illust" role="img" aria-label="家具や荷物を運ぶスタッフと家のイラストが散りばめられた背景"></div>
  <div class="headline">
    <div class="l1">十人いれば十通り。</div>
    <div class="l2">みなさまに最適な</div>
    <div class="l2"><em>遺品整理・生前整理。</em></div>
  </div>
  <div class="hero-scene" role="img" aria-label="トラックに荷物を積み込むスタッフのイラスト"></div>

  <div class="lower"></div>
  <section class="services">
    <article class="card">
      <div class="pic" role="img" aria-label="仏壇や家具が並ぶ部屋のイラスト"></div>
      <div class="label">遺品整理</div>
      <p>故人さまの大切なお品を丁寧に仕分けし、ご遺族さまのお気持ちに寄り添いながら整理いたします。遠方の方や時間のない方もお任せください。ご供養のご相談も承ります。</p>
    </article>
    <article class="card">
      <div class="pic" role="img" aria-label="荷物を整理する人のイラスト"></div>
      <div class="label">生前整理</div>
      <p>施設への入居や住み替えの前に、お元気なうちに身の回りを整えておきませんか。必要な物と不要な物をご一緒に確認し、これからの暮らしを快適にするお手伝いをします。</p>
    </article>
    <article class="card">
      <div class="pic" role="img" aria-label="品物を査定するスタッフのイラスト"></div>
      <div class="label">お買取り</div>
      <p>お家に眠っている骨董品や家電、ブランド品などを専門スタッフが査定いたします。買取り金額を作業費用から差し引くことで、費用を抑えることができます。</p>
    </article>
  </section>

  <section class="recommend">
    <h2>こんな方におすすめします</h2>
    <div class="bubble" style="left:24px">何から手を<br>つけていいのか…<br>知らない業者は不安</div>
    <div class="bubble" style="left:170px">仏壇や神棚を<br>どう処分したら<br>良いか分からない</div>
    <div class="bubble" style="left:318px;top:6px">高齢者や女性<br>だけの世帯なので<br>重い物が運べない</div>
    <div class="bubble" style="left:462px;top:6px">買い取りして<br>もらえる品物が<br>あるか見てほしい</div>
    <div class="person" role="img" aria-label="悩む人物のイラスト" style="left:90px"></div>
    <div class="person" role="img" aria-label="悩む人物のイラスト" style="left:250px"></div>
    <div class="person" role="img" aria-label="悩む人物のイラスト" style="left:400px"></div>
    <div class="free">見積り<br>無料</div>
  </section>

  <div class="footnote">お部屋ひとつからお家まるごと一軒、買取りや供養のご相談もどうぞお気軽にご相談ください。</div>

  <footer class="bottom">
    <div class="brand">
      <div class="badge"></div>
      <div class="brand-name">BRIGHT HAND<span>遺品整理のブライトハンド</span></div>
    </div>
    <div class="contact">
      <div class="tel">
        <svg viewBox="0 0 24 24" aria-hidden="true"><circle cx="12" cy="12" r="12" fill="#e4761a"/><path d="M8.5 6.5l2 2.2-1.2 1.6c.8 1.6 2 2.8 3.6 3.6l1.6-1.2 2.2 2-1.2 2c-4.6-.2-8.8-4.4-9-9z" fill="#fff"/></svg>
        0120-456-721
      </div>
      <div class="info"><span><b>受付時間</b>9:00～18:00</span><span>www.brighthand-seiri.jp</span></div>
    </div>
  </footer>
</div>
</body>
</html>
```